Lucia Verde a furniture, interior design and home decor Brand

I need complete stationary for a new brand, business card, postcard, letter head, shipping envelopes, tissue paper, etc... I would like to use copper foil on some of these items. I have a logo design. I would like to see

Furniture,Interior Design & Home Decor

Interior Design

Colors
606060
7f7f7f

Must have
• My signature style is spanish medeterrenean, my brand colors is charcoal gray with copper. Would love to see a wrought iron panel illustration created, I have attahced a few samples of wrought iron illustration I am attracted to, also an example of packing that has the pattern in foil.
Should not have
• Will not be using the word Design, only Lucia Verde and LV icon

```html
<!DOCTYPE html>
<html lang="en">
<head>
<meta charset="utf-8">
<title>Lucia Verde Stationery</title>
<link href="https://fonts.googleapis.com/css2?family=Open+Sans:wght@400;600&display=swap" rel="stylesheet">
<style>
:root{
  --copper:#d2703a;
  --copper-light:#eca57a;
  --copper-dark:#b8562a;
  --charcoal:#606060;
  --grey:#7f7f7f;
  --ink:#3a3a3a;
  --paper:#ffffff;
  --faint:#c8c8c8;
  --bg:#ffffff;
}
*{margin:0;padding:0;box-sizing:border-box}
html,body{width:1200px;height:1031px;overflow:hidden;background:var(--bg);font-family:"Open Sans",sans-serif;color:var(--ink)}
.canvas{position:relative;width:1200px;height:1031px}
.abs{position:absolute}

/* brand name */
.brand{display:flex;align-items:center;gap:10px;position:absolute}
.brand-dot{width:38px;height:38px;border-radius:50%;border:2px solid var(--copper)}
.brand-name{font-family:"Open Sans",sans-serif;font-weight:400;font-size:26px;color:var(--copper);white-space:nowrap}

/* letterhead */
.letterhead{left:477px;top:63px;width:582px;height:882px;background:var(--paper);border:1px solid #e2e2e2}
.letterhead .rule{position:absolute;left:82px;top:113px;width:487px;height:2px;background:var(--charcoal)}
.contact{position:absolute;text-align:right;font-size:10.5px;line-height:14px;color:var(--ink)}
.contact li{list-style:none;display:flex;justify-content:flex-end;align-items:center;gap:8px}
.contact .ico{width:8px;height:7px;background:var(--copper-dark);display:inline-block}
.contact .ico.round{border-radius:50%;height:8px}
.recipient{position:absolute;left:82px;top:167px;font-size:11px;line-height:18px}
.salute{position:absolute;left:82px;top:314px;font-size:11px}
.body-copy{position:absolute;left:82px;top:334px;width:487px;font-size:11px;line-height:19.5px;text-align:justify}
.letterhead .foot-text{position:absolute;left:0;width:100%;top:810px;text-align:center;font-size:13px;color:var(--charcoal)}
.letterhead .band{position:absolute;left:0;bottom:0;width:100%;height:36px;background:var(--grey)}

/* business card */
.card{left:45px;top:142px;width:378px;height:206px;background:var(--paper);overflow:hidden;border:1px solid #e2e2e2}
.card .top{position:absolute;left:0;top:0;width:100%;height:98px;background:linear-gradient(160deg,var(--copper-dark) 0%,var(--copper) 35%,var(--copper-light) 55%,var(--copper) 75%,var(--copper-dark) 100%)}
.card .brand-dot{border-color:#fff;width:34px;height:34px}
.card .brand-name{color:#fff;font-size:22px}
.card .person{position:absolute;right:22px;top:57px;text-align:right;color:#4a2a1a}
.card .person .name{font-size:13px;font-weight:600;letter-spacing:.5px}
.card .person .title{font-size:9px;letter-spacing:2px}
.card .info{position:absolute;font-size:10px;line-height:13px;color:var(--ink)}
.card .band{position:absolute;left:0;bottom:0;width:100%;height:27px;background:var(--grey)}
.card .web{position:absolute;left:95px;bottom:0;width:188px;height:27px;display:flex;align-items:center;justify-content:center;font-size:9.5px;color:#fff}

/* envelope */
.envelope{left:63px;top:502px;width:767px;height:343px}
.envelope .flap{position:absolute;left:0;top:0;width:767px;height:56px}
.envelope .front{position:absolute;left:0;top:56px;width:767px;height:287px;background:var(--paper);border:1px solid #e2e2e2}
.envelope .window{position:absolute;left:37px;top:159px;width:263px;height:78px;border:2px solid var(--faint);border-radius:10px}
.envelope .band{position:absolute;left:0;bottom:0;width:100%;height:20px;background:var(--grey)}
.envelope .faint .brand-dot{border-color:var(--faint);width:70px;height:70px}
.envelope .faint .brand-name{color:var(--faint);font-size:44px}
</style>
</head>
<body>
<div class="canvas">

  <section class="letterhead abs" aria-label="Letterhead">
    <div class="brand" style="left:82px;top:48px"><span class="brand-dot"></span><span class="brand-name">Lucia Verde</span></div>
    <ul class="contact" style="right:17px;top:4px;padding-top:0;margin-top:0">
      <li style="margin-top:0">+44 (0) 222-5551 <span class="ico"></span></li>
      <li>+44 (0) 222-4444 <span class="ico"></span></li>
      <li>www.ssssss.com <span class="ico round"></span></li>
      <li>aaaaaa@nnn.com <span class="ico"></span></li>
    </ul>
    <div class="rule"></div>
    <div class="recipient">Trenz Pruca<br>Title<br>Company Name<br>4321 First Street<br>Anytown, State ZIP<br>Date 1/30/12</div>
    <p class="salute">Dear Trenz,</p>
    <p class="body-copy">Lorem ipsum dolor sit amet, consectetur adipiscing elit, set eiusmod tempor incidunt et labore et dolore magna aliquam. Ut enim ad minim veniam, quis nostrud exerc. Irure dolor in reprehend incididunt ut labore et dolore magna aliqua. Ut enim ad minim is nostrud exercitation ullam mmodo consequet. Duis aute in voluptate velit esse cillum dolore eu fugiat nulla pariatur. At vver eos et accusam dignissum qui blandit est praesent. Trenz pruca beynoc-regular yourlo of basolu ammolus rasoluguon monugor or trenz ucugwo jag scannar. Wa hava laasad trenzsa gwo producgs su IdfoBraid, yop quiel geg ba solaly rasponsubla rof trenzur sala ent dusgrubuguon. Offoctivo immoriatoly, hawrgasi pwicos asi sirucor. Thas sirutciun applios tyu thuso itoms ghuso pwicos gosi sirucor in mixent gosi sirucor ic mixent ples cak ontisi sowios uf Zerm hawr rwivos. Unte af phen neige pheings atoot Prexs eis phat eit sakem eit vory gast te Plok peish ba useing phen roxas. Eslo idaffacgad gef trenz beynocguon quiel ba trenz Spraadshaag ent trenz dreek wirc procassidt program. Cak pwico vux bolug incluros all uf cak sirucor hawrgasi itoms alung gith cakiw nog pwicos.</p>
    <p class="body-copy" style="top:698px">Plloaso mako nuto uf cakso dodtos anr koop a cupy uf cak vux noaw yerw phuno. Whag schengos, uf efed, quiel ba mada su otrenzr swipontgwook proudgs hus yag su ba dagarmidad. Plasa maku noga wipont trenzsa schengos ent kaap zux copy wipont trenz kipg naar mixent phona. Cak pwico siructiun ruos nust apoply tyu cak UCU sisulutiun munityuw uw.</p>
    <p class="foot-text">City, State Name, 77 Street Name</p>
    <div class="band"></div>
  </section>

  <section class="card abs" aria-label="Business card">
    <div class="top"></div>
    <div class="brand" style="left:33px;top:28px"><span class="brand-dot"></span><span class="brand-name">Lucia Verde</span></div>
    <div class="person"><div class="name">PERSONS NAME</div><div class="title">PERSONS TITLE</div></div>
    <div class="info" style="left:13px;top:149px">
      <div style="display:flex;align-items:center;gap:8px"><svg width="8" height="9" viewBox="0 0 8 9"><path d="M1 0h2l1 2-1 1a5 5 0 0 0 2 2l1-1 2 1v2l-1 1C3 8 0 5 0 1z" fill="var(--copper-dark)"/></svg>(999) 222-5555</div>
      <div style="display:flex;align-items:center;gap:8px"><svg width="8" height="9" viewBox="0 0 8 9"><rect x="1" y="0" width="6" height="9" rx="1" fill="var(--copper-dark)"/></svg>(999) 222-4444</div>
    </div>
    <div class="info" style="right:12px;top:147px;text-align:right">
      <div style="display:flex;align-items:center;justify-content:flex-end;gap:8px">aaaaaa@nnn.com <svg width="9" height="7" viewBox="0 0 9 7"><rect width="9" height="7" fill="var(--copper-dark)"/></svg></div>
      <div style="display:flex;align-items:center;justify-content:flex-end;gap:8px">City, State Name, 77 Street Name <svg width="8" height="10" viewBox="0 0 8 10"><path d="M4 10S0 5.5 0 4a4 4 0 0 1 8 0c0 1.5-4 6-4 6z" fill="var(--copper-dark)"/><circle cx="4" cy="4" r="1.5" fill="#fff"/></svg></div>
    </div>
    <div class="band"></div>
    <svg class="abs" style="left:95px;bottom:0" width="188" height="27" viewBox="0 0 188 27"><defs><linearGradient id="cg" x1="0" x2="1"><stop offset="0" stop-color="var(--copper-dark)"/><stop offset=".5" stop-color="var(--copper-light)"/><stop offset="1" stop-color="var(--copper-dark)"/></linearGradient></defs><polygon points="12,0 176,0 188,27 0,27" fill="url(#cg)"/></svg>
    <div class="web">www.ssssss.com</div>
  </section>

  <section class="envelope abs" aria-label="Envelope">
    <svg class="flap" viewBox="0 0 767 56" preserveAspectRatio="none"><polygon points="85,0 767,0 767,56 0,56" fill="var(--grey)"/></svg>
    <div class="front">
      <div class="brand" style="left:53px;top:38px"><span class="brand-dot"></span><span class="brand-name">Lucia Verde</span></div>
      <ul class="contact" style="right:42px;top:35px">
        <li>+44 (0) 222-5551 <span class="ico"></span></li>
        <li>+44 (0) 222-4444 <span class="ico"></span></li>
        <li>www.ssssss.com <span class="ico round"></span></li>
        <li>aaaaaa@nnn.com <span class="ico"></span></li>
      </ul>
      <div class="window"></div>
      <div class="brand faint" style="left:390px;top:142px"><span class="brand-dot"></span><span class="brand-name">Lucia Verde</span></div>
      <div class="band"></div>
    </div>
  </section>

</div>
</body>
</html>
```